independent cleaner, reliable, custom, thorough, trustworthy

Not sure yet if I want single-sided or double sided, so I'm selecting double-sided just in case, but single-sided designs are okay.

Really looking to find the happy medium between personal and professional in a business card design. I end up building comfortable relationships with the people I work for.

Most of my business is through referrals, but I want some business cards to hand out to people who ask for one (and maybe put them on community bulletin boards).

My target market is homeowners and business owners who are looking for a reliable cleaner and are willing to pay a bit more to have excellent quality and someone they trust.

Theme: I have a personal-professional feel since I'm solo, so the theme should reflect that. Trustworthy, personal, simple. I clean up messes.

Hopefully this is enough info, let me know if you have any questions though of course!

Target Market(s)

Homeowners businessowners who are looking for a reliable cleaner, excellent quality trustworthy.

Industry/Entity Type

Cleaning Service

Contact Information for Business Card

Please include this text:
• Delphine Warrow
• independent cleaner
• reliable, custom, thorough
• 604-317-2269
• mtb.warrow@postmail.example

Font styles to use
Serif
Sans Serif

Colors
ffffff
00a990
0492cd
33a6d7
0355a3
3276b5
919191

Requirements
Must have
• Really looking to find the happy medium between personal and professional in a business card design.
• Background: at least 50% white on the side with the most text (coloured accents or shapes are okay)
• I lean more towards simple and clean, solid colours, maybe a gentle gradient
Nice to have
• Not sure yet if I want single-sided or double sided, so I'm selecting double-sided just in case, but single-sided designs are okay.
• Colours: preferably blues and teals for the font and other objects (if any). Open to designer's choice though. I've toyed around with orangey-yellow, but it doesn't feel right and I keep going back to blues/teals
• Also I uploaded a sketch of my signature and initials so you can get a feel for my personality. I'm not expecting this to be included in the design, it's just there.
Should not have
• I don't like a lot of busy-ness or textures
• Also I don't have a logo (not sure where else to specify this)

```html
<!DOCTYPE html>
<html lang="en">
<head>
<meta charset="utf-8">
<title>Delphine Warrow — Independent Cleaner Business Card</title>
<link rel="stylesheet" href="https://fonts.googleapis.com/css2?family=Cinzel:wght@400;600&family=Lato:wght@400&display=swap">
<style>
  :root {
    --backdrop: #3a3532;
    --card-dark: #0b0b0b;
    --card-light: #ffffff;
    --card-edge: #1a1a1a;
    --blue: #0492cd;
    --deep-blue: #0355a3;
    --teal: #00a990;
    --white: #ffffff;
    --ink: #2b2b2b;
    --silver: #c9c9c9;
    --grey: #919191;
  }
  * { margin: 0; padding: 0; box-sizing: border-box; }
  html, body {
    width: 1200px;
    height: 844px;
    overflow: hidden;
    background: var(--backdrop);
  }
  .canvas {
    width: 1200px;
    height: 844px;
    display: flex;
    align-items: center;
    justify-content: center;
    gap: 60px;
  }
  .card {
    position: relative;
    width: 500px;
    height: 286px;
    box-shadow: 0 18px 40px rgba(0,0,0,0.45);
    display: flex;
    flex-direction: column;
    align-items: center;
  }

  /* Contact side: light background, most of the text */
  .card-contact {
    background: var(--card-light);
    padding-top: 46px;
    border-bottom: 10px solid var(--teal);
  }
  .card-contact .brand-name {
    font-family: "Cinzel", Georgia, serif;
    font-weight: 600;
    font-size: 30px;
    letter-spacing: 1px;
    color: var(--teal);
  }
  .tagline {
    margin-top: 8px;
    font-family: "Lato", Arial, sans-serif;
    font-size: 13px;
    letter-spacing: 3px;
    text-transform: uppercase;
    color: var(--grey);
  }
  .contact-list {
    margin-top: 34px;
    list-style: none;
    font-family: "Lato", Arial, sans-serif;
    font-size: 20px;
    line-height: 1.5;
    color: var(--ink);
  }
  .contact-label { color: var(--blue); margin-right: 6px; }

  /* Identity side: dark background */
  .card-identity {
    background: var(--card-dark);
    border: 1px solid var(--card-edge);
    padding-top: 70px;
  }
  .identity-mark {
    display: flex;
    align-items: center;
    gap: 10px;
  }
  .mark-square {
    width: 14px;
    height: 14px;
    background: var(--silver);
  }
  .identity-mark .brand-name {
    font-family: "Cinzel", Georgia, serif;
    font-weight: 600;
    font-size: 26px;
    letter-spacing: 1px;
    color: var(--silver);
  }
  .owner-name {
    margin-top: 40px;
    font-family: "Cinzel", Georgia, serif;
    font-size: 22px;
    letter-spacing: 1.5px;
    color: var(--silver);
  }
  .owner-role {
    margin-top: 4px;
    font-family: "Lato", Arial, sans-serif;
    font-size: 11px;
    letter-spacing: 4px;
    text-transform: uppercase;
    color: var(--grey);
  }
</style>
</head>
<body>
  <main class="canvas">
    <section class="card card-contact" aria-label="Card front with contact details">
      <div class="brand-name">Delphine Warrow</div>
      <div class="tagline">reliable, custom, thorough</div>
      <ul class="contact-list">
        <li><span class="contact-label">P:</span>604-317-2269</li>
        <li><span class="contact-label">E:</span>mtb.warrow@postmail.example</li>
      </ul>
    </section>

    <section class="card card-identity" aria-label="Card back with name and role">
      <div class="identity-mark">
        <span class="mark-square"></span>
        <span class="brand-name">Delphine Warrow</span>
      </div>
      <div class="owner-name">Delphine Warrow</div>
      <div class="owner-role">Independent Cleaner</div>
    </section>
  </main>
</body>
</html>
```